Communication Business Card Design

We offer complete cabling solutions
Data Cabling,Fibre Optic, and Cabling Repairs fault finding
Security camera installation
TV Aerial installation
Security alarm installation
QWV

Industry/Entity Type

Business

Contact Information for Business Card

Threadmore Solutions
ABN 52 918 374 260
EMAIL threadmoresolutions.com.au
Mobile 0418362057
Rob Kesler

```html
<!DOCTYPE html>
<html lang="en">
<head>
<meta charset="utf-8">
<title>Threadmore Solutions – Business Card</title>
<link rel="stylesheet" href="https://fonts.googleapis.com/css2?family=Montserrat:wght@600&family=Arimo:wght@400&display=swap">
<style>
  :root {
    --ink: #1c1a1d;
    --orange: #f39206;
    --paper: #ffffff;
    --backdrop: #ecebe8;
    --text: #222222;
  }
  * { box-sizing: border-box; margin: 0; padding: 0; }
  html, body { width: 1200px; height: 800px; overflow: hidden; }
  body {
    background: var(--backdrop);
    display: flex;
    align-items: center;
    justify-content: center;
    gap: 80px;
  }
  .card {
    width: 330px;
    height: 520px;
    position: relative;
    overflow: hidden;
    box-shadow: 0 8px 24px rgba(0,0,0,0.18);
    background: var(--paper);
  }
  .brand {
    font-family: "Montserrat", sans-serif;
    font-weight: 600;
    color: var(--paper);
    text-align: center;
    font-size: 38px;
    line-height: 1.1;
    letter-spacing: 0.5px;
  }
  .brand-mark {
    display: block;
    width: 34px;
    height: 34px;
    margin: 0 auto 16px;
    background: var(--paper);
  }

  /* Front */
  .card-front .front-top {
    position: absolute; inset: 0 0 150px 0;
    background: var(--ink);
    display: flex; flex-direction: column;
    align-items: center; justify-content: center;
  }
  .card-front .front-band {
    position: absolute; left: 0; right: 0; bottom: 0; height: 150px;
    background: var(--orange);
  }

  /* Back */
  .card-back .back-header {
    height: 175px;
    background: var(--ink);
    display: flex; flex-direction: column;
    align-items: center; justify-content: center;
  }
  .card-back .brand { font-size: 30px; }
  .card-back .brand-mark { width: 26px; height: 26px; margin-bottom: 12px; }
  .holder-name {
    font-family: "Arimo", sans-serif;
    font-size: 24px;
    color: var(--text);
    text-align: center;
    margin-top: 44px;
    letter-spacing: 0.5px;
  }
  .contact-list { list-style: none; margin-top: 18px; }
  .contact-item {
    position: relative;
    height: 70px;
    border-top: 5px solid var(--orange);
  }
  .contact-icon {
    position: absolute;
    left: 26px; top: -20px;
    width: 34px; height: 34px;
  }
  .contact-text {
    position: absolute;
    left: 74px; top: 12px;
    font-family: "Arimo", sans-serif;
    font-size: 13px;
    color: var(--text);
  }
</style>
</head>
<body>

  <section class="card card-front" aria-label="Card front">
    <div class="front-top">
      <span class="brand-mark"></span>
      <div class="brand">Threadmore<br>Solutions</div>
    </div>
    <div class="front-band"></div>
  </section>

  <section class="card card-back" aria-label="Card back">
    <header class="back-header">
      <span class="brand-mark"></span>
      <div class="brand">Threadmore<br>Solutions</div>
    </header>

    <h1 class="holder-name">ROB KESLER</h1>

    <ul class="contact-list">
      <li class="contact-item">
        <svg class="contact-icon" viewBox="0 0 34 34" aria-hidden="true">
          <rect x="7" y="7" width="20" height="20" transform="rotate(45 17 17)" fill="#1c1a1d"/>
          <path d="M13 12c1-1 2-1 2.5 0l1 1.6c.4.6.2 1.2-.4 1.6l-.6.4c.6 1.4 1.6 2.4 3 3l.4-.6c.4-.6 1-.8 1.6-.4l1.6 1c1 .5 1 1.5 0 2.5-1 1-3 1-5.5-1.3S11.7 14.5 13 12z" fill="#fff"/>
        </svg>
        <span class="contact-text">0418362057</span>
      </li>
      <li class="contact-item">
        <svg class="contact-icon" viewBox="0 0 34 34" aria-hidden="true">
          <rect x="7" y="7" width="20" height="20" transform="rotate(45 17 17)" fill="#1c1a1d"/>
          <g fill="none" stroke="#fff" stroke-width="1.2">
            <circle cx="17" cy="17" r="6"/>
            <ellipse cx="17" cy="17" rx="2.6" ry="6"/>
            <line x1="11" y1="17" x2="23" y2="17"/>
          </g>
        </svg>
        <span class="contact-text">threadmoresolutions.com.au</span>
      </li>
      <li class="contact-item">
        <svg class="contact-icon" viewBox="0 0 34 34" aria-hidden="true">
          <rect x="7" y="7" width="20" height="20" transform="rotate(45 17 17)" fill="#1c1a1d"/>
          <g fill="#fff">
            <circle cx="17" cy="12.5" r="1.6"/>
            <circle cx="17" cy="21.5" r="1.6"/>
            <circle cx="12.5" cy="17" r="1.6"/>
            <circle cx="21.5" cy="17" r="1.6"/>
          </g>
        </svg>
        <span class="contact-text">ABN 52 918 374 260</span>
      </li>
    </ul>
  </section>

</body>
</html>
```